Occupational Therapy Clinic Advertisement

Create an advertisement for a magazine. Below I have attached my original ad (Ad 2020.pdf) . I want the ad changed and it should be eye catching. I would like a eye catching graphics added in the ad. It should be a graphic image that applies to education. I am attaching a sample graphic image of that I liked from someone elses ad- it should not be the same- it just is there to show what I like. Please use the same words from my original ad.Dimensions: 3.75in x 10.3 in

Target Market(s)

Parents of School aged children

Requirements
Must have
• Must have eye catching Graphic. Colors should be eye catching for a typed magazine.

```html
<!DOCTYPE html>
<html lang="en">
<head>
<meta charset="utf-8">
<title>Bright Path OT Services – Magazine Ad</title>
<link rel="stylesheet" href="https://fonts.googleapis.com/css2?family=Oswald:wght@600;700&family=Roboto+Condensed:wght@400;700&family=Montserrat:wght@300;500;700&family=Kaushan+Script&display=swap">
<style>
  :root{
    --red:#e0162b;
    --black:#000;
    --ink:#111;
    --white:#fff;
    --paper-top:#fafafa;
    --paper-bottom:#e4e4e4;
    --grey:#777;
  }
  *{box-sizing:border-box;margin:0;padding:0}
  html,body{width:918px;height:1200px;overflow:hidden;background:var(--white)}
  body{position:relative;font-family:"Roboto Condensed",Arial,sans-serif;color:var(--ink)}
  .ad{position:absolute;top:0;width:446px;height:1200px;overflow:hidden;
      background:linear-gradient(180deg,var(--paper-top),var(--paper-bottom));}
  .ad--dark{left:0}
  .ad--light{left:472px}
  .ad--dark .top-field{position:absolute;left:0;top:0;width:100%;height:712px;background:var(--black)}
  .headline{position:absolute;top:22px;left:0;width:100%;text-align:center;
      font-family:"Oswald",Impact,sans-serif;font-weight:700;font-size:46px;line-height:50px;letter-spacing:.2px}
  .questions{position:absolute;top:196px;left:0;width:100%;text-align:center;
      font-family:"Oswald",Impact,sans-serif;font-weight:600;font-size:23px;line-height:27px}
  .questions p{margin-bottom:16px}
  .ad--dark .headline,.ad--dark .questions{color:var(--white)}
  .ad--dark .qmark{color:var(--red)}
  .ad--light .headline,.ad--light .questions{color:var(--red)}
  .art{position:absolute;left:20px;top:332px;width:406px;height:378px;border-radius:6px}
  .ad--dark .art{background:radial-gradient(circle at 50% 55%,#c62030 0%,#7a1820 28%,#555 55%,#1c1c1c 100%)}
  .ad--light .art{background:linear-gradient(160deg,#5fb3e0 0%,#e0c040 30%,#d8334a 60%,#9a3fb0 85%,#4a8f3c 100%);opacity:.85}
  .contact-tab{position:absolute;left:8px;top:722px;background:var(--red);color:var(--white);
      font-family:"Montserrat",Arial,sans-serif;font-weight:700;font-size:19px;padding:1px 18px;border-radius:10px 10px 0 0;letter-spacing:.5px}
  .contact-rule{position:absolute;left:8px;right:0;top:748px;height:3px;background:var(--red)}
  .brand{position:absolute;top:756px;left:0;width:100%;text-align:center;
      font-family:"Montserrat",Arial,sans-serif;font-weight:500;font-size:40px;line-height:44px;color:var(--ink)}
  .brand small{display:block;font-size:23px;line-height:28px;text-align:right;padding-right:40px}
  .yes{position:absolute;top:826px;left:34px;font-family:"Kaushan Script",cursive;font-size:46px;color:var(--red);transform:rotate(-8deg)}
  .promise{position:absolute;top:874px;left:0;width:100%;text-align:center;font-family:"Oswald",Impact,sans-serif;font-weight:600;font-size:20px}
  .promise s{color:var(--grey);text-decoration-color:var(--red);text-decoration-thickness:2px}
  .promise em{font-family:"Kaushan Script",cursive;font-style:normal;font-size:27px;margin-right:6px}
  .details{position:absolute;top:914px;left:0;width:100%;text-align:center;font-size:17px;line-height:22px}
  .details b{font-weight:700}
  .board{font-family:"Montserrat",Arial,sans-serif;font-weight:700;font-size:20px;line-height:30px}
  .small{font-size:14px}
  .person{font-family:"Montserrat",Arial,sans-serif;font-size:20px;line-height:28px}
  .phone{display:flex;justify-content:center;align-items:center;gap:8px;margin-top:6px;
      font-family:"Montserrat",Arial,sans-serif;font-weight:700;font-size:27px;color:var(--red)}
  .email{display:flex;justify-content:center;align-items:center;gap:6px;margin-top:8px;font-size:15px}
  .footer-band{position:absolute;left:0;bottom:0;width:100%;height:52px;background:var(--red);color:var(--white);
      text-align:center;font-size:14px;line-height:20px;padding-top:6px}
  .footer-band b{font-weight:700}
</style>
</head>
<body>

<section class="ad ad--dark">
  <div class="top-field"></div>
  <h1 class="headline">Does your child<br>struggle with<br>Reading/Kriah<span class="qmark">?</span></h1>
  <div class="questions">
    <p>Does your child know the<br>information but fails the test<span class="qmark">?</span></p>
    <p>Does your child have difficulty<br>remembering names and dates<span class="qmark">?</span></p>
  </div>
  <div class="art" role="img" aria-label="Illustration: large red question mark over a red apple with a Hebrew letter, resting on grey books beside a checked box, with white rays on black"></div>
  <div class="contact-tab">CONTACT</div><div class="contact-rule"></div>
  <div class="brand">Bright Path<small>OT SERVICES</small></div>
  <div class="yes">Yes!</div>
  <p class="promise">Your child <s>can</s> <em>will</em> succeed in school!</p>
  <div class="details">
    <p><b>WE EVALUATE:</b> using standardized evaluations</p>
    <p><b>WE TREAT:</b> the underlying processing deficits</p>
    <p>using researched based techniques</p>
    <p><b>AGES:</b> 6-18</p>
    <p class="board">Board of Ed OT RSA's accepted</p>
    <p class="small">For more information:</p>
    <p class="person">Contact <b>Dina Halpern</b> OTR/L</p>
    <p class="phone"><svg width="24" height="24" viewBox="0 0 24 24" aria-hidden="true"><circle cx="12" cy="12" r="12" fill="#e0162b"/><path d="M8 6c1 0 1.6 2 2 3 .3.8-1 1.4-.8 2 .6 1.4 1.7 2.6 3.2 3.3.6.3 1.2-1 2-.8 1 .4 3 1 3 2s-1.4 2.4-2.6 2.4C10 18.5 5.5 14 5.5 8.6 5.5 7.3 7 6 8 6z" fill="#fff"/></svg>(555) 014-2870</p>
    <p class="email"><svg width="16" height="16" viewBox="0 0 16 16" aria-hidden="true"><circle cx="8" cy="8" r="8" fill="#e0162b"/><path d="M4 8 L12 4 L9 12 L8 9 Z" fill="#fff"/></svg>Or email: brightpathot@example.com</p>
  </div>
  <div class="footer-band"><b>Located in Borough Park</b><br>Evaluations done in Borough Park &amp; Staten Island</div>
</section>

<section class="ad ad--light">
  <h1 class="headline">Does your child<br>struggle with<br>Reading/Kriah?</h1>
  <div class="questions">
    <p>Does your child know the<br>information but fails the test?</p>
    <p>Does your child have difficulty<br>remembering names and dates?</p>
  </div>
  <div class="art" role="img" aria-label="Illustration: tall stack of colourful books with ladders, a tablet showing a Hebrew letter and a checked box"></div>
  <div class="contact-tab">CONTACT</div><div class="contact-rule"></div>
  <div class="brand">Bright Path<small>OT SERVICES</small></div>
  <div class="yes">Yes!</div>
  <p class="promise">Your child <s>can</s> <em>will</em> succeed in school!</p>
  <div class="details">
    <p><b>WE EVALUATE:</b> using standardized evaluations</p>
    <p><b>WE TREAT:</b> the underlying processing deficits</p>
    <p>using researched based techniques</p>
    <p><b>AGES:</b> 6-18</p>
    <p class="board">Board of Ed OT RSA's accepted</p>
    <p class="small">For more information:</p>
    <p class="person">Contact <b>Dina Halpern</b> OTR/L</p>
    <p class="phone"><svg width="24" height="24" viewBox="0 0 24 24" aria-hidden="true"><circle cx="12" cy="12" r="12" fill="#e0162b"/><path d="M8 6c1 0 1.6 2 2 3 .3.8-1 1.4-.8 2 .6 1.4 1.7 2.6 3.2 3.3.6.3 1.2-1 2-.8 1 .4 3 1 3 2s-1.4 2.4-2.6 2.4C10 18.5 5.5 14 5.5 8.6 5.5 7.3 7 6 8 6z" fill="#fff"/></svg>(555) 014-2870</p>
    <p class="email"><svg width="16" height="16" viewBox="0 0 16 16" aria-hidden="true"><circle cx="8" cy="8" r="8" fill="#e0162b"/><path d="M4 8 L12 4 L9 12 L8 9 Z" fill="#fff"/></svg>Or email: brightpathot@example.com</p>
  </div>
  <div class="footer-band"><b>Located in Borough Park</b><br>Evaluations done in Borough Park &amp; Staten Island</div>
</section>

</body>
</html>
```